Fahrzeugbeschriftung: Heizung - Sanitär
Zielgruppe
Wir sind ein junger Meisterbetrieb der Heizungs- und Sanitärbranche und im Rhein-Main-Gebiet für unsere Kunden im Einsatz.
Wir benötigen eine Fahrzeugbeschriftung, die auffällig und modern, jedoch nicht zu verspielt und bunt ist.
Die Beschriftung soll für einen weißen Brava M3 Kasten sein. Es sollten alle Seiten des Fahrzeugs beschriftet werden.
Aufgabenstellung
Die Farbgebung sollte sich am dem Farben des Logos orientieren. Das Firmenlogo sollte im Vordergrund stehen. Auch die Worte Heizung, Sanitär, Solar sollten hervorstechen und gut erkennbar sein. Zusätzlich sollte der Begriff Meisterbetrieb verwendet werden.

```html
<!DOCTYPE html>
<html lang="de">
<head>
<meta charset="utf-8">
<title>Halders Haustechnik – Fahrzeugbeschriftung</title>
<link rel="stylesheet" href="https://fonts.googleapis.com/css2?family=Montserrat:wght@600;700;800&display=swap">
<style>
  :root{
    --navy:#123e63;
    --teal:#2a8c99;
    --white:#ffffff;
    --backdrop:#eceff1;
    --edge:#d3d9dd;
  }
  html,body{margin:0;padding:0;overflow:hidden;}
  body{width:776px;height:1200px;background:var(--backdrop);position:relative;font-family:'Montserrat',sans-serif;}
  .livery{position:absolute;display:block;}
  .livery--left{left:18px;top:24px;}
  .livery--right{left:18px;top:326px;}
  .livery--rear{left:128px;top:630px;}
  .panel{fill:var(--white);stroke:var(--edge);stroke-width:1;}
  .band-teal{fill:var(--teal);}
  .band-navy{fill:var(--navy);}
  .service{fill:var(--teal);font-weight:700;letter-spacing:3px;}
  .service--light{fill:var(--white);}
  .wordmark{fill:var(--navy);font-weight:800;}
  .subline{fill:var(--teal);font-weight:700;}
  .phone{font-weight:700;}
  .phone--light{fill:var(--white);}
  .phone--dark{fill:var(--navy);}
  .web{fill:var(--white);font-weight:700;letter-spacing:2px;}
  .brand-square{fill:var(--navy);}
  .brand-name{fill:var(--navy);font-weight:800;}
  .tag{fill:var(--navy);font-weight:600;letter-spacing:1px;}
</style>
</head>
<body>

<!-- Side: driver facing left -->
<svg class="livery livery--left" width="740" height="276" viewBox="0 0 740 276">
  <rect class="panel" x="0.5" y="0.5" width="739" height="275" rx="16"/>
  <polygon class="band-teal" points="190,232 740,118 740,232"/>
  <polygon class="band-navy" points="170,232 740,232 740,262 176,266"/>
  <text class="service" x="340" y="50" font-size="19">• Heizung</text>
  <text class="service" x="340" y="74" font-size="19">• Sanitär</text>
  <text class="service" x="340" y="98" font-size="19">• Solar</text>
  <g transform="rotate(-10 200 190)">
    <text class="wordmark" x="196" y="192" font-size="46">HALDERS</text>
    <text class="subline" x="202" y="222" font-size="22" letter-spacing="8">Haustechnik</text>
  </g>
  <text class="phone phone--light" x="408" y="222" font-size="15">0170-42196608</text>
  <text class="web" x="254" y="254" font-size="13">www.halders-heizung.de</text>
  <rect class="brand-square" x="540" y="58" width="20" height="20"/>
  <text class="brand-name" x="568" y="76" font-size="22">HALDERS</text>
  <text class="tag" x="568" y="96" font-size="11">Meisterbetrieb</text>
</svg>

<!-- Side: driver facing right -->
<svg class="livery livery--right" width="740" height="276" viewBox="0 0 740 276">
  <rect class="panel" x="0.5" y="0.5" width="739" height="275" rx="16"/>
  <polygon class="band-teal" points="0,118 470,232 0,232"/>
  <polygon class="band-navy" points="0,232 570,232 564,266 0,262"/>
  <text class="service" x="270" y="38" font-size="19">• Heizung</text>
  <text class="service" x="270" y="62" font-size="19">• Sanitär</text>
  <text class="service" x="270" y="86" font-size="19">• Solar</text>
  <g transform="rotate(10 260 140)">
    <text class="wordmark" x="262" y="132" font-size="46">HALDERS</text>
    <text class="subline" x="258" y="162" font-size="22" letter-spacing="8">Haustechnik</text>
  </g>
  <text class="phone phone--light" x="205" y="222" font-size="15">0170-42196608</text>
  <text class="web" x="210" y="254" font-size="13">www.halders-heizung.de</text>
  <rect class="brand-square" x="60" y="40" width="20" height="20"/>
  <text class="brand-name" x="88" y="58" font-size="22">HALDERS</text>
  <text class="tag" x="88" y="78" font-size="11">Meisterbetrieb</text>
</svg>

<!-- Rear doors -->
<svg class="livery livery--rear" width="520" height="550" viewBox="0 0 520 550">
  <rect class="panel" x="0.5" y="0.5" width="519" height="549" rx="22"/>
  <rect class="band-teal" x="0" y="350" width="520" height="130"/>
  <path class="band-navy" d="M0,480 H520 V528 Q520,550 498,550 H22 Q0,550 0,528 Z"/>
  <text class="wordmark" x="260" y="74" font-size="56" text-anchor="middle">HALDERS</text>
  <text class="subline" x="260" y="112" font-size="28" letter-spacing="10" text-anchor="middle">Haustechnik</text>
  <text class="phone phone--dark" x="260" y="154" font-size="22" text-anchor="middle">0170-42196608</text>
  <rect class="brand-square" x="40" y="262" width="22" height="22"/>
  <text class="brand-name" x="72" y="282" font-size="24">HALDERS</text>
  <text class="tag" x="72" y="304" font-size="12">Meisterbetrieb</text>
  <text class="service service--light" x="330" y="392" font-size="19">• Heizung</text>
  <text class="service service--light" x="330" y="418" font-size="19">• Sanitär</text>
  <text class="service service--light" x="330" y="444" font-size="19">• Solar</text>
  <text class="web" x="260" y="508" font-size="15" text-anchor="middle">www.halders-heizung.de</text>
</svg>

</body>
</html>
```